ボトル容器(280mL入り・画像参照)のオモテ面のラベルデザインを依頼します。
「食器洗いを楽しく!」というコンセプトを、手肌と環境へのやさしさという要素を盛り込みながら、ラベルのデザインとして表現してください。
パラダイスを感じさせるような、明るく、楽しく、元気でウキウキ、ワクワクするような雰囲気と同時に、予定価格が280mL入で1,300円前後と通常の食器洗剤と比べて高価格帯なので、安っぽさを感じさせない高級感も考慮してください。
当商品は今後、香りのバリエーション展開を予定しているので、ラベルの一部の色を替えることで、複数の香りバリエーションに対応できるデザインを希望します。
ラベルサイズ:幅50mm×高さ75mm以上100mm以下

以下の要素を入れてください。
商品名:Fluvorne
商品名の読み:フルヴォーン
品名:台所用せっけん
香り:○○○の香り
メインキャッチコピー:食器洗いを楽しく!
サブキャッチコピー:手肌と環境を守る水せっけん
シンプル 複雑
単色 カラフル
暗い 明るい
日常 高級
遊び心 厳粛
未来的 伝統的
女性的 男性的
• 高解像度JPG (.jpg)
• イラストレーター形式 (.ai)
添付画像のボトルに貼られたラベルのサイズは幅50mm×高さ75mmです。

コンセプトを最もよく表現していただいた提案でした。

とてもレベルの高い提案ばかりで、たいへん感謝しております。ありがとうございました。

```html
<!DOCTYPE html>
<html lang="ja">
<head>
<meta charset="utf-8">
<title>Fluvorne Kitchen soap labels</title>
<link href="https://fonts.googleapis.com/css2?family=Cinzel:wght@500;700&family=Parisienne&family=Noto+Serif+JP:wght@500;700&family=Noto+Sans+JP:wght@500;700&family=Libre+Baskerville:wght@700&display=swap" rel="stylesheet">
<style>
  :root{
    --page:#eef0f1;
    --paper:#ffffff;
    --ink:#2b3a40;
    --brand:#1f8f9c;
    --badge:#f7e43a;
    --badge-ink:#2a78c8;
    --frame:#9fd4dc;
  }
  *{margin:0;padding:0;box-sizing:border-box}
  html,body{width:890px;height:1200px;overflow:hidden;background:var(--page)}
  .sheet{position:relative;width:890px;height:1200px;display:flex;justify-content:center;align-items:center;gap:30px}
  .label{
    --accent:#6fc3ea;
    --accent-soft:#d6eefa;
    position:relative;width:400px;height:600px;background:var(--paper);
    box-shadow:0 2px 10px rgba(0,0,0,.08);overflow:hidden;color:var(--ink);
  }
  .label--aloe{--accent:#8cc66a;--accent-soft:#e3f2d6}
  .label__frame{position:absolute;inset:10px;border:1.5px solid var(--frame);pointer-events:none}
  .label__type{position:absolute;top:34px;left:0;width:300px;text-align:center;font:500 15px "Noto Serif JP",serif;letter-spacing:2px}
  .label__script{position:absolute;top:52px;left:0;width:300px;text-align:center;font:400 40px "Parisienne",cursive;color:var(--brand)}
  .label__sub{position:absolute;top:114px;left:0;width:400px;text-align:center;font:700 19px "Noto Serif JP",serif;letter-spacing:1px}
  .badge{
    position:absolute;top:18px;right:18px;width:104px;height:104px;border-radius:50%;
    background:var(--badge);display:flex;align-items:center;justify-content:center;text-align:center;
    font:700 17px/1.3 "Noto Sans JP",sans-serif;color:var(--badge-ink);transform:rotate(-8deg);
  }
  .flourish{position:absolute;top:148px;left:60px;width:280px;height:30px;
    background:linear-gradient(90deg,transparent,var(--frame),transparent);opacity:.6;border-radius:15px}
  .brand{position:absolute;top:186px;left:0;width:400px;text-align:center;font:700 54px "Cinzel",serif;color:var(--brand);letter-spacing:2px}
  .brand__kana{position:absolute;top:252px;left:0;width:400px;text-align:center;font:500 14px "Noto Serif JP",serif;letter-spacing:3px;color:var(--brand)}
  .story{position:absolute;top:284px;left:28px;width:318px;font:700 11.5px/1.45 "Libre Baskerville",serif;color:var(--ink)}
  .motif{position:absolute;left:10px;bottom:10px;width:250px;height:150px;
    background:radial-gradient(ellipse at 20% 90%,var(--accent) 0%,var(--accent-soft) 55%,transparent 80%)}
  .scent{position:absolute;right:10px;bottom:10px;width:34px;height:170px;background:var(--accent);
    color:#fff;writing-mode:vertical-rl;font:700 15px "Noto Sans JP",sans-serif;letter-spacing:3px;
    display:flex;align-items:center;justify-content:center}
</style>
</head>
<body>
<main class="sheet">
  <article class="label label--savon">
    <div class="label__frame"></div>
    <p class="label__type">台所用せっけん</p>
    <p class="label__script">Kitchen soap</p>
    <div class="badge">食器洗いを<br>楽しく!</div>
    <p class="label__sub">手肌と環境を守る水せっけん</p>
    <div class="flourish" role="img" aria-label="Decorative scroll flourish"></div>
    <h1 class="brand">FLUVORNE</h1>
    <p class="brand__kana">フルヴォーン</p>
    <p class="story">There is a sense that it wants to change the time like being in bright fun Paradise, the time of housework with the stress, such as dishwashing and fluvorne is a kitchen for environmentally friendly soap and hand skin. Do not use ingredients that cause rough hands and petroleum-based synthetic surfactant. I am using only plant-based natural ingredients and soap.</p>
    <div class="motif" role="img" aria-label="Soap bubbles illustration"></div>
    <p class="scent">シャボンの香り</p>
  </article>

  <article class="label label--aloe">
    <div class="label__frame"></div>
    <p class="label__type">台所用せっけん</p>
    <p class="label__script">Kitchen soap</p>
    <div class="badge">食器洗いを<br>楽しく!</div>
    <p class="label__sub">手肌と環境を守る水せっけん</p>
    <div class="flourish" role="img" aria-label="Decorative scroll flourish"></div>
    <h1 class="brand">FLUVORNE</h1>
    <p class="brand__kana">フルヴォーン</p>
    <p class="story">There is a sense that it wants to change the time like being in bright fun Paradise, the time of housework with the stress, such as dishwashing and fluvorne is a kitchen for environmentally friendly soap and hand skin. Do not use ingredients that cause rough hands and petroleum-based synthetic surfactant. I am using only plant-based natural ingredients and soap.</p>
    <div class="motif" role="img" aria-label="Aloe leaves illustration"></div>
    <p class="scent">アロエの香り</p>
  </article>
</main>
</body>
</html>
```